Psychologist Banner Ads for Remarketing & yarnwave

Brand awareness campaign for tallowbridge.com.au

// Ad Formats //
Static JPEG
Max 45KB in file size
All ads must have a border

// Ad Sizes //
Static: (for Zindle Display network) 300×250, 160×600, 728×90
Static: (for Yarnwave, no more than 25% text): 600×315, 1200 x 627

Please use logo, image and "maximise your wellbeing" from the website home page.

```html
<!DOCTYPE html>
<html lang="en">
<head>
<meta charset="utf-8">
<title>Tallowbridge Psychology – Maximise Your Wellbeing Banner Set</title>
<link rel="stylesheet" href="https://fonts.googleapis.com/css2?family=Alfa+Slab+One&family=Arimo:wght@400;700&display=swap">
<style>
  :root {
    --stage: #ececec;
    --ad-bg: #ffffff;
    --ad-border: #0b0b0b;
    --navy: #123e8f;
    --royal: #1a55b3;
    --sky: #1d8fdb;
    --swoosh-light: #5aa7e6;
    --photo-top: #cfe6f5;
    --photo-mid: #e9eff3;
    --photo-warm: #d9b9a0;
    --brand: #1f4f9a;
  }
  * { box-sizing: border-box; margin: 0; padding: 0; }
  html, body { width: 1200px; height: 900px; overflow: hidden; }
  body {
    background: var(--stage);
    position: relative;
    font-family: "Arimo", Arial, sans-serif;
  }
  .ad {
    position: absolute;
    background: var(--ad-bg);
    border: 3px solid var(--ad-border);
    overflow: hidden;
  }
  .ad__photo {
    position: absolute;
    background: linear-gradient(160deg, var(--photo-top) 0%, var(--photo-mid) 55%, var(--photo-warm) 100%);
  }
  .ad__swoosh { position: absolute; inset: 0; width: 100%; height: 100%; }
  .headline {
    font-family: "Alfa Slab One", "Rockwell", serif;
    color: var(--navy);
    letter-spacing: 0.5px;
    line-height: 1;
    text-transform: uppercase;
  }
  .tagline {
    color: var(--sky);
    font-weight: 400;
    line-height: 1.15;
  }
  .brand {
    color: var(--brand);
    font-weight: 700;
    line-height: 1.05;
    text-align: center;
  }
  .brand span { display: block; }

  /* Leaderboard 728×90 */
  .ad--leaderboard { left: 146px; top: 40px; width: 850px; height: 104px; }
  .ad--leaderboard .brand { position: absolute; left: 18px; top: 24px; font-size: 19px; text-align: left; }
  .ad--leaderboard .brand span:last-child { font-size: 12px; letter-spacing: 2px; }
  .ad--leaderboard .copy { position: absolute; left: 215px; top: 14px; width: 310px; text-align: center; }
  .ad--leaderboard .headline { font-size: 37px; }
  .ad--leaderboard .tagline { font-size: 23px; margin-top: 4px; }
  .ad--leaderboard .ad__photo {
    left: 500px; top: 0; width: 350px; height: 104px;
    clip-path: path("M0 0 C60 22 100 72 140 104 L350 104 L350 0 Z");
  }

  /* Medium rectangle 300×250 */
  .ad--rectangle { left: 326px; top: 308px; width: 350px; height: 292px; }
  .ad--rectangle .ad__photo {
    left: 0; top: 0; width: 350px; height: 160px;
    clip-path: path("M0 0 L350 0 L350 120 Q180 168 0 92 Z");
  }
  .ad--rectangle .copy { position: absolute; left: 0; right: 0; top: 168px; text-align: center; }
  .ad--rectangle .headline { font-size: 32px; }
  .ad--rectangle .tagline { font-size: 23px; margin-top: 2px; }
  .ad--rectangle .brand { position: absolute; left: 0; right: 0; top: 236px; font-size: 17px; }
  .ad--rectangle .brand span:last-child { font-size: 10px; letter-spacing: 2px; }

  /* Skyscraper 160×600 */
  .ad--skyscraper { left: 813px; top: 168px; width: 186px; height: 700px; }
  .ad--skyscraper .ad__photo {
    left: 0; top: 0; width: 186px; height: 330px;
    clip-path: path("M0 0 L186 0 L186 318 Q100 330 0 276 Z");
  }
  .ad--skyscraper .copy { position: absolute; left: 0; right: 0; top: 430px; text-align: center; }
  .ad--skyscraper .headline { font-size: 23px; }
  .ad--skyscraper .tagline { font-size: 27px; margin-top: 10px; line-height: 1.45; }
  .ad--skyscraper .brand { position: absolute; left: 0; right: 0; top: 600px; font-size: 20px; }
  .ad--skyscraper .brand span:last-child { font-size: 11px; letter-spacing: 2px; }
</style>
</head>
<body>

  <section class="ad ad--leaderboard" aria-label="Leaderboard banner 728 by 90">
    <div class="ad__photo" role="img" aria-label="Photo of a smiling woman with arms raised against a bright sky"></div>
    <svg class="ad__swoosh" viewBox="0 0 850 104" aria-hidden="true">
      <path d="M520 0 C580 22 620 72 660 104" fill="none" stroke="var(--royal)" stroke-width="11"/>
      <path d="M545 0 C600 22 640 70 680 104" fill="none" stroke="var(--swoosh-light)" stroke-width="4"/>
    </svg>
    <p class="brand"><span>Tallowbridge</span><span>PSYCHOLOGY</span></p>
    <div class="copy">
      <h1 class="headline">Maximise</h1>
      <p class="tagline">Your Wellbeing</p>
    </div>
  </section>

  <section class="ad ad--rectangle" aria-label="Medium rectangle banner 300 by 250">
    <div class="ad__photo" role="img" aria-label="Photo of a smiling woman with arms raised against a bright sky"></div>
    <svg class="ad__swoosh" viewBox="0 0 350 292" aria-hidden="true">
      <path d="M0 92 Q180 168 350 120" fill="none" stroke="var(--royal)" stroke-width="10"/>
      <path d="M0 102 Q180 176 350 130" fill="none" stroke="var(--swoosh-light)" stroke-width="3"/>
    </svg>
    <div class="copy">
      <h2 class="headline">Maximise</h2>
      <p class="tagline">Your Wellbeing</p>
    </div>
    <p class="brand"><span>Tallowbridge</span><span>PSYCHOLOGY</span></p>
  </section>

  <section class="ad ad--skyscraper" aria-label="Skyscraper banner 160 by 600">
    <div class="ad__photo" role="img" aria-label="Photo of a smiling woman with arms raised against a bright sky"></div>
    <svg class="ad__swoosh" viewBox="0 0 186 700" aria-hidden="true">
      <path d="M0 276 Q100 330 186 318" fill="none" stroke="var(--royal)" stroke-width="10"/>
      <path d="M0 287 Q100 340 186 328" fill="none" stroke="var(--swoosh-light)" stroke-width="3"/>
    </svg>
    <div class="copy">
      <h2 class="headline">Maximise</h2>
      <p class="tagline">Your<br>Wellbeing</p>
    </div>
    <p class="brand"><span>Tallowbridge</span><span>PSYCHOLOGY</span></p>
  </section>

</body>
</html>
```